Stonebay Towing Business Card

Towing
Accident towing
Mechanical breakdown
Insurance, salvage and recovery
4wd off road towing
Light & Heavy towing
8347 2516
24 hour business 7 days

Logo can be whole size on front

Industry/Entity Type

Towing/ transport

Contact Information for Business Card

The above

```html
<!DOCTYPE html>
<html lang="en">
<head>
<meta charset="utf-8">
<title>Stonebay Towing Business Card</title>
<link href="https://fonts.googleapis.com/css2?family=Roboto:wght@500;700;900&display=swap" rel="stylesheet">
<style>
  :root {
    --backdrop: #3a3a3b;
    --card: #232427;
    --red: #d71f27;
    --white: #f4f4f4;
    --muted: #8a8a8c;
  }
  * { box-sizing: border-box; margin: 0; padding: 0; }
  html, body { width: 1200px; height: 694px; overflow: hidden; }
  body {
    background: var(--backdrop);
    font-family: "Roboto", Arial, sans-serif;
    position: relative;
  }
  .card {
    position: absolute;
    top: 204px;
    width: 500px;
    height: 286px;
    background: var(--card);
    border-radius: 0 120px 0 120px;
  }
  .card--front { left: 60px; }
  .card--back { left: 640px; }

  .brand-front {
    position: absolute;
    inset: 0;
    display: flex;
    align-items: center;
    justify-content: center;
    gap: 14px;
  }
  .brand-front .brand-dot {
    width: 22px; height: 22px; border-radius: 50%;
    background: var(--red);
  }
  .brand-front .brand-name {
    color: var(--red);
    font-weight: 900;
    font-size: 50px;
    letter-spacing: -0.5px;
  }

  .brand-back {
    position: absolute;
    top: 36px;
    right: 44px;
    color: var(--red);
    font-weight: 900;
    font-size: 22px;
  }

  .services-title {
    position: absolute;
    left: 38px;
    top: 96px;
    color: var(--white);
    font-weight: 700;
    font-size: 14px;
    line-height: 17px;
    text-transform: uppercase;
  }
  .services-title .accent { color: var(--red); }
  .services-title::after {
    content: "";
    display: block;
    width: 44px;
    height: 3px;
    margin-top: 7px;
    background: var(--red);
  }

  .service-list {
    position: absolute;
    list-style: none;
    color: var(--white);
    font-weight: 700;
    font-size: 11.5px;
    line-height: 20px;
    text-transform: uppercase;
  }
  .service-list li { display: flex; align-items: center; gap: 10px; }
  .service-list li::before {
    content: "";
    width: 7px; height: 7px; border-radius: 50%;
    background: var(--red);
    flex: none;
  }
  .service-list--primary { left: 38px; top: 150px; }
  .service-list--secondary { left: 250px; top: 80px; }

  .phone {
    position: absolute;
    left: 38px;
    top: 222px;
    display: flex;
    align-items: center;
    gap: 12px;
    color: var(--red);
    font-weight: 700;
    font-size: 34px;
    letter-spacing: 1px;
  }
  .phone svg { width: 30px; height: 30px; }

  .divider {
    position: absolute;
    left: 270px;
    top: 160px;
    height: 44px;
    border-left: 1px dashed var(--muted);
  }
  .hours {
    position: absolute;
    left: 288px;
    top: 162px;
    color: var(--white);
    font-weight: 700;
    font-size: 14px;
    line-height: 18px;
    text-transform: uppercase;
  }
</style>
</head>
<body>
  <section class="card card--front" aria-label="Card front">
    <div class="brand-front">
      <span class="brand-dot"></span>
      <span class="brand-name">Stonebay Towing</span>
    </div>
  </section>

  <section class="card card--back" aria-label="Card back">
    <div class="brand-back">Stonebay Towing</div>

    <h2 class="services-title">Our <span class="accent">One Stop</span><br>Towing Services</h2>

    <ul class="service-list service-list--primary">
      <li>Towing</li>
      <li>Accident towing</li>
      <li>Mechanical breakdown</li>
    </ul>

    <ul class="service-list service-list--secondary">
      <li>Insurance, salvage and recovery</li>
      <li>4WD off road towing</li>
      <li>Light &amp; heavy towing</li>
    </ul>

    <div class="phone">
      <svg viewBox="0 0 30 30" aria-hidden="true">
        <path d="M4 20c0-4 5-6 11-6s11 2 11 6l-1 4h-5l-1-4c-3-1-5-1-8 0l-1 4H5z" fill="#f4f4f4"/>
        <path d="M9 10a9 9 0 0 1 12 0M6 7a13 13 0 0 1 18 0" stroke="#f4f4f4" stroke-width="2" fill="none" stroke-linecap="round"/>
      </svg>
      <span>8347 2516</span>
    </div>

    <span class="divider"></span>
    <p class="hours">24 Hour Business<br>And 7 Days</p>
  </section>
</body>
</html>
```